Annual review for The Heron Collective

The Heron Collective is a small public relations agency in London specialising in corporate and public affairs. Most of our work is international and we have a strong connection to South Africa. We would like to prepare a short annual review for 2016. The review will serve as both a review of our activities in 2016, and as a credentials document. Content then will include:
1. An introduction to the business
2. Who we are
3. Projects and clients undertaken in 2016
4. News and views
We imagine it will be used mostly as a pdf but would like it to be suitable for print. We envisage it to be about 8 pages long. The design look and feel should convey a business, while small, of stature. We shall include some of our client logos but we would welcome the use of some photography / imagery to have visual impact (although we don't have very much of our own!). The corporate look and feel is white, grey and black.

Industry/Entity Type

Public Relation

Font styles to use
Sans Serif

Requirements
Must have
• My project must convey a business with flair and gravitas, that punches above its weight.
Nice to have
• Thoughtful use of imagery.

```html
<!DOCTYPE html>
<html lang="en">
<head>
<meta charset="utf-8">
<title>The Heron Collective — Annual Review 2016</title>
<link rel="stylesheet" href="https://fonts.googleapis.com/css2?family=Montserrat:wght@700&family=Lato:wght@400;700;900&family=Oswald:wght@700&family=Lora:wght@400&display=swap">
<style>
  :root {
    --canvas: #ebebeb;
    --paper: #ffffff;
    --ink: #111111;
    --ink-soft: #1e1e1e;
    --grey-dark: #555555;
    --grey-mid: #9a9a9a;
    --grey-light: #d6d6d6;
    --text-on-dark: #ffffff;
  }
  * { box-sizing: border-box; margin: 0; padding: 0; }
  html, body { width: 1200px; height: 848px; overflow: hidden; background: var(--canvas); }
  .spread { position: relative; width: 1200px; height: 848px; }

  .page {
    position: absolute; top: 56px; width: 523px; height: 740px;
    background: var(--paper); overflow: hidden;
    box-shadow: 0 2px 6px rgba(0,0,0,.35);
  }
  .page--front { left: 54px; }
  .page--back { left: 618px; }

  .layer { position: absolute; inset: 0; width: 100%; height: 100%; }
  .photo { position: absolute; }

  /* Front cover */
  .front-office-photo {
    left: 0; top: 180px; width: 523px; height: 380px;
    background: linear-gradient(180deg, rgba(235,235,235,0) 0%, #ececec 30%, #e6e6e6 70%, rgba(230,230,230,0) 100%);
  }
  .front-portrait {
    left: 270px; top: 100px; width: 253px; height: 500px;
    background: linear-gradient(180deg, #b9b9b9 0%, #6a6a6a 35%, #3a3a3a 70%, #4a3a34 100%);
  }
  .brand {
    position: absolute; display: flex; align-items: center; gap: 14px; white-space: nowrap;
    font-family: "Montserrat", sans-serif; font-weight: 700; font-size: 26px; letter-spacing: -0.2px;
  }
  .brand__mark { width: 30px; height: 30px; border-radius: 50%; border: 2px solid currentColor; }
  .brand--front { left: 90px; top: 26px; color: var(--text-on-dark); }
  .brand--back { left: 90px; top: 241px; color: var(--grey-dark); }

  .welcome-card {
    position: absolute; left: 27px; top: 183px; width: 228px; height: 119px;
    border: 1.5px solid var(--grey-dark); border-radius: 10px;
    background: rgba(255,255,255,.94); text-align: center;
    font-family: "Lato", sans-serif; color: var(--ink); white-space: nowrap;
  }
  .welcome-card__title { font-weight: 900; font-size: 31px; margin-top: 14px; line-height: 1; }
  .welcome-card__sub {
    font-size: 14.5px; margin: 9px 12px 0; padding-bottom: 5px;
    border-bottom: 1px solid var(--grey-dark); text-transform: uppercase; letter-spacing: -0.2px;
  }
  .welcome-card__address { font-size: 12.5px; margin-top: 7px; }

  .review-label {
    position: absolute; left: 35px; top: 500px; white-space: nowrap;
    font-family: "Lora", serif; font-size: 26px; color: var(--text-on-dark);
  }
  .review-year {
    position: absolute; left: 32px; top: 532px;
    font-family: "Oswald", sans-serif; font-weight: 700; font-size: 82px; line-height: 1;
    color: var(--grey-light); letter-spacing: -1px;
  }
  .intro {
    position: absolute; left: 33px; top: 630px; width: 452px;
    font-family: "Lato", sans-serif; font-weight: 700; font-size: 10.2px; line-height: 1.3;
    color: var(--text-on-dark);
  }
  .web-pill {
    position: absolute; width: 283px; height: 26px;
    border: 1.5px solid var(--text-on-dark); border-radius: 13px;
    display: flex; align-items: center; justify-content: center;
    font-family: "Lato", sans-serif; font-size: 10.5px; letter-spacing: 5.4px;
    color: var(--text-on-dark); white-space: nowrap;
  }
  .page--front .web-pill { left: 121px; top: 686px; }
  .page--back .web-pill { left: 120px; top: 680px; }

  /* Back cover */
  .back-office-photo {
    left: 58px; top: 352px; width: 408px; height: 268px;
    background: radial-gradient(ellipse at 55% 45%, #e4e1df 0%, #f0eeed 50%, rgba(255,255,255,0) 80%);
  }
  .contact {
    position: absolute; left: 0; width: 100%; top: 298px; text-align: center;
    font-family: "Lato", sans-serif; font-size: 14px; line-height: 23px; color: var(--ink);
  }
</style>
</head>
<body>
<main class="spread">

  <section class="page page--front">
    <div class="photo front-office-photo" role="img" aria-label="Faint photo of colleagues working together at office desks"></div>
    <div class="photo front-portrait" role="img" aria-label="Portrait photo of a businessman in a dark suit holding a leather folder"></div>

    <svg class="layer" viewBox="0 0 523 740" aria-hidden="true">
      <defs>
        <linearGradient id="fold" x1="0" y1="0" x2="1" y2="1">
          <stop offset="0" stop-color="#ffffff"/>
          <stop offset="1" stop-color="#bdbdbd"/>
        </linearGradient>
      </defs>
      <polygon points="0,34 166,124 270,112 270,100 0,100" fill="var(--paper)"/>
      <polygon points="330,122 523,96 523,150" fill="var(--grey-mid)"/>
      <polygon points="0,0 523,0 523,72 166,124 0,34" fill="var(--ink)"/>
      <polygon points="0,404 90,376 322,608 200,452" fill="url(#fold)"/>
      <polygon points="0,404 200,452 322,608 523,496 523,740 0,740" fill="var(--ink-soft)"/>
    </svg>

    <div class="brand brand--front"><span class="brand__mark"></span>The Heron Collective</div>

    <div class="welcome-card">
      <p class="welcome-card__title">WELCOME</p>
      <p class="welcome-card__sub">Introducing The Heron</p>
      <p class="welcome-card__address">24 Harlow Street London W1K 3PN</p>
    </div>

    <p class="review-label">Annual review</p>
    <p class="review-year">2016</p>
    <p class="intro">The Heron Collective is a public affairs and policy advisory firm based in London. In a highly regulated policy environment, we provide corporate and public affairs consultancy advice as well as corporate responsibility and sustainable development policy expertise.</p>
    <p class="web-pill">www.heroncollective.com</p>
  </section>

  <section class="page page--back">
    <svg class="layer" viewBox="0 0 523 740" aria-hidden="true">
      <defs>
        <linearGradient id="haze" x1="0" y1="0" x2="0" y2="1">
          <stop offset="0" stop-color="#f3f3f3"/>
          <stop offset="1" stop-color="#ffffff"/>
        </linearGradient>
      </defs>
      <rect x="0" y="0" width="523" height="260" fill="url(#haze)"/>
    </svg>

    <div class="photo back-office-photo" role="img" aria-label="Faint photo of a team gathered around a computer in a bright office"></div>

    <svg class="layer" viewBox="0 0 523 740" aria-hidden="true">
      <polygon points="0,696 262,594 523,696 523,740 0,740" fill="var(--ink-soft)"/>
    </svg>

    <div class="brand brand--back"><span class="brand__mark"></span>The Heron Collective</div>
    <div class="contact">
      <p>Addres: 24 Harlow Street London W1K 3PN</p>
      <p>Email:&nbsp; hello@heroncollective.com</p>
    </div>
    <p class="web-pill">www.heroncollective.com</p>
  </section>

</main>
</body>
</html>
```